Business Card Design Project

Looking for a logo and business card for a Real State Business i will be opening. The name is not choosen yet , but will probably be RKT IMOVEIS.
I was thinking black and silver colors, but am open to nice ideas.
I did add a business card that i liked a lot, am looking for something like that, with logo in black or silver in a black card. The logo i was thinking in the letters RKT as i uploaded or something or little and cute buildings or a house...just ideas, can be any nice logo.
Updates

You guys can add other colors if you want, I like colors very "BRIGHT" and "open", like red, pink, strong colors. almost glow in the dark colors. lol

Designers,

I've increased more 88 dollars in the budget for 1st place cause I will want envelope designs... small and big sizes.

So 1st place is now U$248,00. 

No need to send the envelope designs right now... only the business cards designs.

Thank you.

Industry/Entity Type

Business

Requirements
Must have
• Patricia Souza Ramos

www.RKTimoveisx.com.br

+554193817462

patricia@rktimoveisx.com.br

```html
<!DOCTYPE html>
<html lang="pt-BR">
<head>
<meta charset="UTF-8">
<title>RKT Imóveis — Cartão de visita</title>
<link href="https://fonts.googleapis.com/css2?family=Arimo:wght@400;700&display=swap" rel="stylesheet">
<style>
  :root {
    --page: #ffffff;
    --card: #0b0a06;
    --accent: #f28c00;
    --ink: #ffffff;
  }
  * { margin: 0; padding: 0; box-sizing: border-box; }
  html, body {
    width: 1000px;
    height: 1200px;
    overflow: hidden;
    background: var(--page);
    font-family: "Arimo", Arial, sans-serif;
  }
  .sheet { position: relative; width: 1000px; height: 1200px; }
  .card {
    position: absolute;
    left: 92px;
    width: 816px;
    background: var(--card);
    overflow: hidden;
  }
  .card--front { top: 110px; height: 472px; }
  .card--back { top: 620px; height: 470px; }

  .brand-name {
    position: absolute;
    color: var(--accent);
    font-weight: 400;
    line-height: 1;
    letter-spacing: 0.01em;
  }
  .card--front .brand-name {
    left: 118px;
    top: 218px;
    font-size: 54px;
  }
  .divider {
    position: absolute;
    left: 314px;
    top: 78px;
    width: 4px;
    height: 314px;
    background: var(--accent);
  }
  .contact {
    position: absolute;
    left: 392px;
    top: 140px;
    color: var(--ink);
    font-weight: 700;
  }
  .contact__name {
    color: var(--accent);
    font-size: 27px;
    line-height: 1;
    margin-bottom: 20px;
  }
  .contact__line {
    font-size: 19px;
    line-height: 30px;
    letter-spacing: 0.01em;
  }
  .contact__web {
    margin-top: 56px;
    font-size: 19px;
    letter-spacing: 0.01em;
  }
  .card--back .brand-name {
    left: 0;
    right: 0;
    top: 210px;
    text-align: center;
    font-size: 132px;
  }
</style>
</head>
<body>
<main class="sheet">
  <section class="card card--front">
    <div class="brand-name">RKT</div>
    <div class="divider"></div>
    <div class="contact">
      <p class="contact__name">Patricia Souza Ramos</p>
      <p class="contact__line">patricia@rktimoveisx.com.br</p>
      <p class="contact__line">0055 419 381 7462</p>
      <p class="contact__web">www.RKTimoveisx.com.br</p>
    </div>
  </section>
  <section class="card card--back">
    <div class="brand-name">RKT</div>
  </section>
</main>
</body>
</html>
```